Business card design needed for rebranded top-end landscaping business

We need a new business card design, incorporating our logo (colours Green #8dc63f and Grey #8a8c8e) and also some options that include the colour dark navy (eg #000040) as our uniforms are navy with white and grey trim.

We are an innovative landscaping company that maintains high-end gardens for meticulous clients. We pride ourselves on our customer service, our professionalism, and our workmanship.

Our business name needs to be easily read and our branding needs to be bold and memorable, without screaming "tradesman"! We prefer clean lines over lots of fine detail.

The design MUST include:
- Business name ("Brambleton Gardenworks")
- Logo (file uploaded)
- Employee name
- Phone number
- Email address
- www.brambletongardenworks.com.au
- Facebook & Instagram logos
- The Turfcraft Guild logo (file uploaded) along with the word "Member"
- Licence "Lic. 618392K"

OPTIONAL inclusions:
- "Creating outdoor spaces for our community to be inspired, refreshed and re-energised"
- "Landscape Maintenance - Irrigation - Arboriculture" (dashes can be replaced with dots or other)
- "Fully qualified, licensed & insured"
- "Residential - Strata - Commercial - Real Estate" (dashes can be replaced with dots or other)

High-end professionals and retirees, real estate agents

Landscaping

See Project description

Sans Serif

Designer to choose colors to be used in the design.

• Must incorporate our logo, and colours Green #8dc63f and Grey #8a8c8e) from the logo, and the colour DARK NAVY (eg #000040).
• The design MUST include:
• - Business name ("Brambleton Gardenworks")
• - Logo (file uploaded)
• - Employee name
• - Phone number
• - Email address
• - www.brambletongardenworks.com.au
• - Facebook & Instagram logos
• - The Turfcraft Guild logo (file uploaded) along with the word "Member"
• - Licence "Lic. 618392K"
• OPTIONAL inclusions:
• - "Creating outdoor spaces for our community to be inspired, refreshed and re-energised"
• - "Landscape Maintenance - Irrigation - Arboriculture" (dashes can be replaced with dots or other)
• - "Fully qualified, licensed & insured"
• - "Residential - Strata - Commercial - Real Estate" (dashes can be replaced with dots or other)

```html
<!DOCTYPE html>
<html lang="en">
<head>
<meta charset="utf-8">
<title>Brambleton Gardenworks – Business Card</title>
<link rel="stylesheet" href="https://fonts.googleapis.com/css2?family=Montserrat:wght@400;500;600;700&family=Roboto:wght@400;500&display=swap">
<style>
  :root {
    --green: #8dc63f;
    --grey: #8a8c8e;
    --ink: #3a3b3d;
    --card: #f4f4f3;
    --panel: #dedfe0;
    --backdrop: #6e5843;
  }
  * { margin: 0; padding: 0; box-sizing: border-box; }
  html, body { width: 900px; height: 1200px; overflow: hidden; }
  body { background: var(--backdrop); position: relative; font-family: "Montserrat", sans-serif; color: var(--ink); }

  .card { position: absolute; background: var(--card); border-radius: 16px; overflow: hidden; box-shadow: 0 6px 14px rgba(0,0,0,.35); }
  .card--front { left: 78px; top: 137px; width: 762px; height: 431px; }
  .card--back { left: 76px; top: 630px; width: 767px; height: 436px; }

  .licence { position: absolute; left: 41px; top: 42px; font-size: 20px; font-weight: 500; letter-spacing: .5px; color: var(--ink); }
  .social { position: absolute; top: 36px; right: 44px; display: flex; gap: 22px; }
  .social__dot { width: 42px; height: 42px; border: 3px solid var(--green); border-radius: 50%; }

  .brand { position: absolute; display: flex; flex-direction: column; align-items: center; }
  .brand__mark { border-radius: 50%; background: var(--grey); }
  .brand__name { color: var(--grey); font-weight: 600; white-space: nowrap; }
  .card--front .brand { left: 0; right: 0; top: 90px; }
  .card--front .brand__mark { width: 116px; height: 116px; }
  .card--front .brand__name { font-size: 38px; margin-top: 36px; }

  .services { position: absolute; left: 0; right: 0; bottom: 0; height: 66px; background: var(--green); display: flex; align-items: center; padding-left: 44px; font-size: 19.5px; font-weight: 500; color: var(--ink); letter-spacing: .3px; }

  .card--back .brand { left: 30px; width: 260px; top: 48px; }
  .card--back .brand__mark { width: 84px; height: 84px; }
  .card--back .brand__name { font-size: 20px; margin-top: 30px; }

  .person { position: absolute; right: 43px; top: 84px; text-align: right; font-family: "Roboto", sans-serif; }
  .person__name { color: var(--green); font-size: 30px; font-weight: 500; letter-spacing: 1px; }
  .person__role { color: var(--ink); font-size: 24px; letter-spacing: 1px; }

  .contact-panel { position: absolute; left: 0; right: 0; bottom: 0; height: 200px; background: var(--panel); }
  .contacts { position: absolute; left: 32px; top: 52px; list-style: none; font-family: "Roboto", sans-serif; font-size: 19.5px; color: var(--ink); }
  .contacts li { display: flex; align-items: center; height: 34px; }
  .contacts svg { width: 22px; height: 22px; margin-right: 12px; fill: var(--green); }
  .divider { position: absolute; left: 479px; top: 42px; width: 2px; height: 124px; background: var(--grey); }

  .guild { position: absolute; left: 526px; width: 196px; top: 46px; display: flex; flex-direction: column; align-items: center; }
  .guild__mark { width: 40px; height: 40px; background: var(--green); }
  .guild__name { margin-top: 14px; font-size: 17px; font-weight: 500; letter-spacing: 1px; white-space: nowrap; }
  .guild__member { margin-top: 10px; width: 196px; height: 20px; background: var(--green); color: var(--ink); font-size: 13px; font-weight: 700; letter-spacing: 12px; text-align: center; line-height: 20px; padding-left: 12px; }
</style>
</head>
<body>
  <section class="card card--front">
    <p class="licence">LIC. 618392K</p>
    <div class="social" aria-label="Social media">
      <span class="social__dot"></span>
      <span class="social__dot"></span>
    </div>
    <div class="brand">
      <span class="brand__mark"></span>
      <span class="brand__name">Brambleton Gardenworks</span>
    </div>
    <p class="services">LANDSCAPE MAINTENANCE - IRRIGATION - ARBORICULTURE</p>
  </section>

  <section class="card card--back">
    <div class="brand">
      <span class="brand__mark"></span>
      <span class="brand__name">Brambleton Gardenworks</span>
    </div>
    <div class="person">
      <p class="person__name">HARRIET LOWE</p>
      <p class="person__role">OWNER</p>
    </div>
    <div class="contact-panel">
      <ul class="contacts">
        <li><svg viewBox="0 0 24 24"><path d="M3 9c0-3 4-5 9-5s9 2 9 5l-4 1-1-3H8L7 10zM6 11h12l2 8H4z"/></svg>013 579 2468</li>
        <li><svg viewBox="0 0 24 24"><path d="M2 5h20v3l-10 6L2 8zM2 10l10 6 10-6v9H2z"/></svg>email@brambletongardenworks.com.au</li>
        <li><svg viewBox="0 0 24 24"><path d="M12 2a10 10 0 1 0 0 20 10 10 0 0 0 0-20zm0 2c1.5 1.6 2.4 4 2.6 7H9.4c.2-3 1.1-5.4 2.6-7zM4.1 11a8 8 0 0 1 4.6-6.3C7.9 6.5 7.5 8.6 7.4 11zm0 2h3.3c.1 2.4.5 4.5 1.3 6.3A8 8 0 0 1 4.1 13zm5.3 0h5.2c-.2 3-1.1 5.4-2.6 7-1.5-1.6-2.4-4-2.6-7zm7.2 0h3.3a8 8 0 0 1-4.6 6.3c.8-1.8 1.2-3.9 1.3-6.3zm0-2c-.1-2.4-.5-4.5-1.3-6.3a8 8 0 0 1 4.6 6.3z"/></svg>www.brambletongardenworks.com.au</li>
      </ul>
      <span class="divider"></span>
      <div class="guild">
        <span class="guild__mark"></span>
        <p class="guild__name">THE TURFCRAFT GUILD</p>
        <p class="guild__member">MEMBER</p>
      </div>
    </div>
  </section>
</body>
</html>
```